Dravetti Business Cards

We need a business card design for Dravetti Mining.

This is a B2B company that buys and sells large machinery tires within the coal mining industry. The design should the strong, crisp and masculine. I have uploaded the company logo and rough mock-up of what the back of the card should look like. the front of the card should have the same look/feel as the back. I need editable templates for both the front and the back of the card.

Color scheme should be grey/green/black

Contact information to include on the card:
Name: Owen Pellsworth
Title: Managing Director
Phone: 972-555-0143
Address: 3157 Brantley #5 Dallas, TX 75209
Email: Owen@Dravetti-example.com

I am also opening a contest for letterhead design. If you submit a business card design, please also submit a letterhead design with the same look/feel. The winner of the business card design will also will the letter head and be paid for both.

Target Market(s)

Procurement men/women in the coal mining industry

Industry/Entity Type

Coal Mining

```html
<!DOCTYPE html>
<html lang="en">
<head>
<meta charset="utf-8">
<title>Dravetti Mining – Business Cards</title>
<link rel="stylesheet" href="https://fonts.googleapis.com/css2?family=Michroma&family=Questrial&display=swap">
<style>
  :root {
    --card-dark: #333436;
    --card-dark-deep: #2a2b2d;
    --brand-green: #5cb31c;
    --text-white: #ffffff;
    --page-bg: #ffffff;
  }
  * { margin: 0; padding: 0; box-sizing: border-box; }
  html, body {
    width: 1130px; height: 1200px; overflow: hidden;
    background: var(--page-bg);
  }
  .canvas { position: relative; width: 1130px; height: 1200px; }

  .card {
    position: absolute; left: 0; width: 1130px;
    border-radius: 26px; overflow: hidden;
    background: var(--card-dark);
  }

  /* Front */
  .card-front { top: 0; height: 561px; }
  .front-texture {
    position: absolute; left: 0; right: 0; top: 375px; bottom: 0;
    background: linear-gradient(180deg, #38393b 0%, var(--card-dark-deep) 100%);
  }
  .brand {
    position: absolute; top: 138px; left: 0; right: 0;
    display: flex; justify-content: center; align-items: center; gap: 22px;
  }
  .brand-square { width: 56px; height: 56px; background: var(--brand-green); }
  .brand-name {
    font-family: "Michroma", sans-serif; font-size: 40px;
    color: var(--text-white); letter-spacing: 1px;
  }
  .website {
    position: absolute; top: 272px; left: 0; right: 0; text-align: center;
    font-family: "Questrial", sans-serif; font-size: 34px; color: var(--text-white);
  }
  .website .accent { color: var(--brand-green); }

  /* Back */
  .card-back { top: 631px; height: 569px; }
  .back-header { position: absolute; left: 0; right: 0; top: 0; height: 202px; }
  .back-body {
    position: absolute; left: 0; right: 0; top: 202px; bottom: 0;
    background: var(--brand-green);
  }
  .person-name {
    position: absolute; top: 86px; left: 0; right: 0; text-align: center;
    font-family: "Michroma", sans-serif; font-size: 33px;
    color: var(--text-white); letter-spacing: 2px;
  }
  .person-title {
    position: absolute; top: 138px; left: 0; right: 0; text-align: center;
    font-family: "Michroma", sans-serif; font-size: 20px;
    color: var(--text-white); letter-spacing: 3px;
  }
  .contact-list {
    position: absolute; top: 360px; left: 0; right: 0;
    list-style: none;
    font-family: "Michroma", sans-serif; font-size: 23px;
    color: var(--text-white); letter-spacing: 2px;
  }
  .contact-list li {
    height: 41px; display: flex; justify-content: center; align-items: center; gap: 10px;
  }
  .contact-icon { width: 24px; height: 24px; fill: var(--text-white); flex: none; }
</style>
</head>
<body>
<div class="canvas">

  <section class="card card-front" aria-label="Card front">
    <div class="front-texture" role="img" aria-label="Dark embossed square texture band"></div>
    <div class="brand">
      <span class="brand-square"></span>
      <span class="brand-name">DRAVETTI MINING</span>
    </div>
    <p class="website">www.<span class="accent">dravetti-example</span>.com</p>
  </section>

  <section class="card card-back" aria-label="Card back">
    <div class="back-header">
      <h1 class="person-name">OWEN PELLSWORTH</h1>
      <p class="person-title">MANAGING DIRECTOR</p>
    </div>
    <div class="back-body"></div>
    <ul class="contact-list">
      <li>
        <svg class="contact-icon" viewBox="0 0 24 24" aria-hidden="true"><path d="M12 3 2 12h3v9h5v-6h4v6h5v-9h3z"/></svg>
        3157 BRANTLEY #5 DALLAS, TX 75209
      </li>
      <li>
        <svg class="contact-icon" viewBox="0 0 24 24" aria-hidden="true"><path d="M8 2h8a2 2 0 0 1 2 2v16a2 2 0 0 1-2 2H8a2 2 0 0 1-2-2V4a2 2 0 0 1 2-2zm0 3v13h8V5zm3 14.5h2v1h-2z"/></svg>
        972 555 0143
      </li>
      <li>
        <svg class="contact-icon" viewBox="0 0 24 24" aria-hidden="true"><path d="M3 6h18v12H3zm1.5 1.2v.4L12 13l7.5-5.4v-.4z"/></svg>
        OWEN@DRAVETTI-EXAMPLE.COM
      </li>
      <li>
        <svg class="contact-icon" viewBox="0 0 24 24" aria-hidden="true"><path d="M12 2a10 10 0 1 0 0 20 10 10 0 0 0 0-20zm0 2c.9 1.2 1.6 2.6 2 4h-4c.4-1.4 1.1-2.8 2-4zM4.3 14a8 8 0 0 1 0-4h3.5a16 16 0 0 0 0 4zm.8 2h3c.3 1.3.8 2.5 1.4 3.6A8 8 0 0 1 5.1 16zm3-8h-3a8 8 0 0 1 4.4-3.6C8.9 5.5 8.4 6.7 8.1 8zM12 20c-.9-1.2-1.6-2.6-2-4h4c-.4 1.4-1.1 2.8-2 4zm2.3-6H9.7a14 14 0 0 1 0-4h4.6a14 14 0 0 1 0 4zm.2 5.6c.6-1.1 1.1-2.3 1.4-3.6h3a8 8 0 0 1-4.4 3.6zm1.7-5.6a16 16 0 0 0 0-4h3.5a8 8 0 0 1 0 4z"/></svg>
        DRAVETTI-EXAMPLE.COM
      </li>
    </ul>
  </section>

</div>
</body>
</html>
```